Full service meeting planning company needs new business cards

Velmora Linkway is a full service meeting planning company that specializes in on-line conference registration web development and event communications. We combine citywide hotel management, mobile applications, eblast reminders, confirmation letters, and customized reporting to create a seamless registration process. We also manage group motor coach transportation, food and beverages, entertainment, stage and lighting for group of 10 to 4000.

Target Market(s)

Corporations and associations

Industry/Entity Type

Event Planning

Contact Information for Business Card

standard size 3.5" wide and 2" tall

Font styles to use
Serif
Sans Serif

Colors
f37122
f78f20
333333
5c5c5c
9d9d9d
f68d4d

Requirements
Must have
• {name}
• Velmora Linkway
• P.O. Box 7384, Grand Rapids, M I 49568
• www.velmoralinkway.com
• {email}
• {phone}
• {mobile phone}
Nice to have
• Our colors are black, grey and orange as an accent color
Should not have
• I am not happy with our website layout anymore either. It feels dark and old but it does explain who we are pretty well if you'd like to review; www.velmoralinkway.com

```html
<!DOCTYPE html>
<html lang="en">
<head>
<meta charset="utf-8">
<title>Velmora Linkway – Business Card</title>
<link href="https://fonts.googleapis.com/css2?family=Montserrat:wght@500;600&family=Open+Sans:wght@400;600&display=swap" rel="stylesheet">
<style>
  :root {
    --orange: #f37122;
    --orange-light: #f78f20;
    --gold: #f2b52e;
    --ink: #333333;
    --grey: #5c5c5c;
    --grey-light: #9d9d9d;
    --paper: #ffffff;
    --paper-shade: #ececec;
    --backdrop: #e9e6e1;
  }
  * { margin: 0; padding: 0; box-sizing: border-box; }
  html, body { width: 1200px; height: 1023px; overflow: hidden; }
  body {
    background: var(--backdrop);
    font-family: "Open Sans", Arial, sans-serif;
    position: relative;
  }
  .card {
    position: absolute;
    left: 250px;
    width: 700px;
    height: 400px;
    border-radius: 22px;
    overflow: hidden;
    box-shadow: 0 10px 28px rgba(0,0,0,0.18);
  }
  .card--front {
    top: 70px;
    background: linear-gradient(135deg, var(--paper-shade) 0%, var(--paper) 45%, #f6f6f6 100%);
    border-bottom: 6px solid var(--orange-light);
  }
  .card--back {
    top: 550px;
    background: radial-gradient(ellipse at 70% 40%, var(--gold) 0%, var(--orange-light) 55%, #dd7d14 100%);
  }
  .brand {
    position: absolute;
    left: 62px;
    top: 62px;
    display: flex;
    align-items: center;
    gap: 22px;
  }
  .brand__dot {
    width: 96px;
    height: 96px;
    border-radius: 50%;
    background: var(--orange-light);
  }
  .brand__name {
    font-family: "Montserrat", Arial, sans-serif;
    font-weight: 600;
    font-size: 36px;
    letter-spacing: 0.5px;
    color: var(--orange-light);
    text-transform: uppercase;
  }
  .person {
    position: absolute;
    left: 180px;
    top: 262px;
    text-align: right;
    width: 140px;
  }
  .person__name {
    font-size: 30px;
    color: var(--grey);
    line-height: 1.1;
    letter-spacing: 0.5px;
  }
  .person__title {
    font-size: 15px;
    color: var(--orange-light);
    letter-spacing: 1px;
  }
  .divider {
    position: absolute;
    left: 345px;
    top: 240px;
    width: 1px;
    height: 120px;
    background: var(--orange-light);
    opacity: 0.6;
  }
  .contact {
    position: absolute;
    left: 365px;
    top: 244px;
    list-style: none;
    font-size: 14px;
    color: var(--grey);
    letter-spacing: 0.8px;
  }
  .contact li {
    display: flex;
    align-items: center;
    gap: 10px;
    height: 28px;
  }
  .contact svg { width: 14px; height: 14px; flex: none; }
  .back__name {
    position: absolute;
    left: 0; right: 0;
    top: 170px;
    text-align: center;
    font-family: "Montserrat", Arial, sans-serif;
    font-weight: 600;
    font-size: 44px;
    letter-spacing: 1px;
    color: var(--paper);
    text-transform: uppercase;
  }
  .back__url {
    position: absolute;
    left: 28px;
    top: 200px;
    transform: translate(-50%, -50%) rotate(90deg);
    transform-origin: center;
    margin-left: 20px;
    white-space: nowrap;
    font-size: 15px;
    letter-spacing: 4px;
    color: var(--paper);
  }
</style>
</head>
<body>

<section class="card card--front">
  <div class="brand">
    <div class="brand__dot"></div>
    <div class="brand__name">Velmora Linkway</div>
  </div>

  <div class="person">
    <div class="person__name">Your Name</div>
    <div class="person__title">Title</div>
  </div>

  <div class="divider"></div>

  <ul class="contact">
    <li>
      <svg viewBox="0 0 14 14"><circle cx="7" cy="7" r="6" fill="none" stroke="#f78f20" stroke-width="1.4"/><path d="M4.5 4 l1.5 0 l0.6 1.6 l-0.9 0.7 a4 4 0 0 0 2 2 l0.7-0.9 l1.6 0.6 l0 1.5 a5.5 5.5 0 0 1 -5.5 -5.5z" fill="#f78f20"/></svg>
      616 555 0142
    </li>
    <li>
      <svg viewBox="0 0 14 14"><rect x="3.5" y="1" width="7" height="12" rx="1.3" fill="none" stroke="#f78f20" stroke-width="1.4"/><circle cx="7" cy="11" r="0.8" fill="#f78f20"/></svg>
      616 555 0187
    </li>
    <li>
      <svg viewBox="0 0 14 14"><rect x="1" y="3" width="12" height="8" fill="none" stroke="#f78f20" stroke-width="1.4"/><path d="M1 3 l6 5 l6 -5" fill="none" stroke="#f78f20" stroke-width="1.4"/></svg>
      info@velmoralinkway.com
    </li>
    <li>
      <svg viewBox="0 0 14 14"><path d="M7 13 C3 8 2.5 6.5 2.5 5 a4.5 4.5 0 0 1 9 0 c0 1.5 -0.5 3 -4.5 8z" fill="#f78f20"/><circle cx="7" cy="5" r="1.6" fill="#fff"/></svg>
      P.O. Box 7384, Grand Rapids, M I 49568
    </li>
  </ul>
</section>

<section class="card card--back">
  <div class="back__url">www.velmoralinkway.com</div>
  <div class="back__name">Velmora Linkway</div>
</section>

</body>
</html>
```